Valtora

Standard Business Card design.
Sample two-sided design uploaded. White front, Black back.
Would like white shield to be on all black background side.
Willing to look at a couple creative designs, but nothing crazy.
Preference for a classic, confident, strong design.

```html
<!DOCTYPE html>
<html lang="en">
<head>
<meta charset="utf-8">
<title>Valtora Business Card</title>
<link rel="stylesheet" href="https://fonts.googleapis.com/css2?family=Arimo:wght@400;700&display=swap">
<style>
  :root {
    --stage: #151515;
    --card: #2b2b2c;
    --card-edge: #333334;
    --ink: #ffffff;
    --ink-soft: #e6e6e6;
    --emboss: #49494b;
    --emboss-faint: #363638;
  }
  * { box-sizing: border-box; margin: 0; padding: 0; }
  html, body {
    width: 1200px;
    height: 874px;
    overflow: hidden;
    background: var(--stage);
    font-family: "Arimo", Arial, sans-serif;
  }
  .canvas {
    position: relative;
    width: 1200px;
    height: 874px;
  }
  .card {
    position: absolute;
    left: 320px;
    width: 560px;
    height: 320px;
    border-radius: 18px;
    background: var(--card);
    border: 1px solid var(--card-edge);
    overflow: hidden;
  }
  .card-back { top: 97px; }
  .card-front { top: 457px; }

  .back-brand {
    position: absolute;
    left: 0;
    right: 0;
    top: 70px;
    display: flex;
    flex-direction: column;
    align-items: center;
    gap: 26px;
  }
  .back-brand-mark {
    width: 80px;
    height: 80px;
    background: var(--emboss);
  }
  .back-wordmark {
    font-size: 52px;
    font-weight: 700;
    letter-spacing: 6px;
    line-height: 1;
    color: var(--emboss);
  }

  .front-accent {
    position: absolute;
    left: 300px;
    top: 84px;
    width: 270px;
    height: 270px;
    background: var(--emboss-faint);
  }
  .front-brand {
    position: absolute;
    left: 30px;
    top: 28px;
    display: flex;
    align-items: center;
    gap: 12px;
  }
  .front-brand-mark {
    width: 26px;
    height: 26px;
    background: var(--ink);
  }
  .front-wordmark {
    font-size: 34px;
    font-weight: 700;
    letter-spacing: 4px;
    line-height: 1;
    color: var(--ink);
  }
  .person {
    position: absolute;
    left: 30px;
    top: 92px;
    color: var(--ink);
  }
  .person-name {
    font-size: 23px;
    font-weight: 400;
    letter-spacing: 1px;
  }
  .person-title {
    margin-top: 3px;
    font-size: 12px;
    color: var(--ink-soft);
  }
  .address {
    position: absolute;
    left: 30px;
    top: 162px;
    font-size: 14px;
    font-style: normal;
    line-height: 18px;
    color: var(--ink-soft);
  }
  .contacts {
    position: absolute;
    left: 30px;
    top: 206px;
    list-style: none;
    font-size: 14px;
    line-height: 19px;
    color: var(--ink-soft);
  }
  .contacts li {
    display: flex;
    align-items: center;
    gap: 8px;
  }
  .contacts svg {
    width: 11px;
    height: 11px;
    fill: var(--ink-soft);
    flex: none;
  }
</style>
</head>
<body>
<main class="canvas">
  <section class="card card-back" aria-label="Card back">
    <div class="back-brand">
      <div class="back-brand-mark" aria-hidden="true"></div>
      <div class="back-wordmark">VALTORA</div>
    </div>
  </section>

  <section class="card card-front" aria-label="Card front">
    <div class="front-accent" aria-hidden="true"></div>
    <div class="front-brand">
      <div class="front-brand-mark" aria-hidden="true"></div>
      <div class="front-wordmark">VALTORA</div>
    </div>
    <div class="person">
      <div class="person-name">DANIEL HARTWELL</div>
      <div class="person-title">President</div>
    </div>
    <address class="address">
      4412 Cedar Ridge Road<br>
      Kelston, Canada 58213
    </address>
    <ul class="contacts">
      <li>
        <svg viewBox="0 0 24 24" aria-hidden="true"><path d="M6.6 10.8a15.1 15.1 0 0 0 6.6 6.6l2.2-2.2a1 1 0 0 1 1-.25 11.4 11.4 0 0 0 3.6.57 1 1 0 0 1 1 1V20a1 1 0 0 1-1 1A17 17 0 0 1 3 4a1 1 0 0 1 1-1h3.5a1 1 0 0 1 1 1c0 1.25.2 2.45.57 3.6a1 1 0 0 1-.25 1z"/></svg>
        555-214-8830
      </li>
      <li>
        <svg viewBox="0 0 24 24" aria-hidden="true"><path d="M7 1h10a2 2 0 0 1 2 2v18a2 2 0 0 1-2 2H7a2 2 0 0 1-2-2V3a2 2 0 0 1 2-2zm0 3v14h10V4zm5 15.5a1.2 1.2 0 1 0 0 2.4 1.2 1.2 0 0 0 0-2.4z"/></svg>
        555-907-4162
      </li>
      <li>
        <svg viewBox="0 0 24 24" aria-hidden="true"><path d="M2 5h20v14H2zm2 2v.5l8 5 8-5V7l-8 5z"/></svg>
        info@valtora.com
      </li>
      <li>
        <svg viewBox="0 0 24 24" aria-hidden="true"><circle cx="12" cy="12" r="10"/></svg>
        www.valtora.com
      </li>
    </ul>
  </section>
</main>
</body>
</html>
```